Letterhead for New Orthopaedic Surgery Practice

My husband and I are starting our own practice named RB Spine & Vitality Center. We would like to create a nice simple but high class letterhead that doesn't use too much solid color ink when printing. I like the colors dark blue, gold, yellow. Open to other suggestions. We will need to list him and I both on the top of the letterhead. Here is the important information:
Lucinda Perrow, M.D. - Hand and Upper Extremity Surgery
Abena Quist, M.D. - Hip & Knee Replacement/General Orthopaedic Surgery
Location: 18735 North Harlow Pkwy
Coral Springs, NC 27614
Phone: 954-218-4650
Fax: 954-582-1346
Email: info@myrbspine.com

The only thing is that the phone and fax numbers will change once we get into our space. I just want to get the design started. I am including several documents which are my previous practice letterhead, my current procedure room letterhead, and our new Logo. The other letterheads are just for examples but please think outside of the box! We would love to see some great designs.

Colors
0054AA
0677BA
7BADD7
CADEEF
E8F1F8
0094D4
00A9DD
6FCCEA
C7EBF8
E9F6FB

Requirements
Must have
• class, elegance, luxury

```html
<!DOCTYPE html>
<html lang="en">
<head>
<meta charset="utf-8">
<title>RB Spine &amp; Vitality Center — Letterhead</title>
<link href="https://fonts.googleapis.com/css2?family=Montserrat:wght@400;500;600&display=swap" rel="stylesheet">
<style>
  :root {
    --navy: #0b3f86;
    --royal: #0054aa;
    --cyan: #0094d4;
    --violet: #2e3f9a;
    --paper: #f4f5f6;
    --ink: #1d1f24;
    --backdrop: #dfe2e7;
  }
  * { margin: 0; padding: 0; box-sizing: border-box; }
  html, body {
    width: 1200px; height: 900px; overflow: hidden;
    background: var(--backdrop);
    font-family: "Montserrat", sans-serif;
  }
  .letterhead {
    position: absolute; left: 300px; top: 12px;
    width: 600px; height: 876px;
    background: var(--paper);
    overflow: hidden;
    box-shadow: 0 6px 20px rgba(0,0,0,.18);
  }
  .header-shapes, .footer-shapes { position: absolute; left: 0; width: 600px; }
  .header-shapes { top: 0; height: 200px; }
  .footer-shapes { bottom: 0; height: 200px; }
  .brand {
    position: absolute; top: 40px; right: 36px;
    display: flex; align-items: center; gap: 8px;
    color: #fff; font-weight: 500; font-size: 13px;
    letter-spacing: .06em; text-transform: uppercase;
  }
  .brand-dot { width: 10px; height: 10px; border-radius: 50%; background: #fff; }
  .physicians { position: absolute; left: 48px; top: 214px; }
  .physician { margin-bottom: 6px; }
  .physician-name {
    color: var(--royal); font-weight: 600; font-size: 13px;
    letter-spacing: .03em; text-transform: uppercase; line-height: 1.3;
  }
  .physician-specialty { color: var(--ink); font-size: 11.5px; line-height: 1.3; }
  .contact {
    position: absolute; left: 88px; bottom: 62px;
    color: var(--ink); font-size: 15px; font-weight: 500;
    line-height: 30px; list-style: none;
  }
</style>
</head>
<body>
  <main class="letterhead">
    <svg class="header-shapes" viewBox="0 0 600 200" aria-hidden="true">
      <polygon points="0,0 320,0 0,196" fill="var(--royal)"/>
      <polygon points="150,0 600,0 600,118 400,124 130,178" fill="var(--navy)"/>
      <polygon points="400,118 560,118 548,132 392,136" fill="var(--violet)"/>
      <polygon points="130,178 372,142 390,162 60,196" fill="var(--cyan)"/>
    </svg>

    <div class="brand"><span class="brand-dot"></span>RB Spine &amp; Vitality Center</div>

    <section class="physicians">
      <div class="physician">
        <p class="physician-name">Lucinda Perrow, M.D.</p>
        <p class="physician-specialty">Hand and Upper Extremity Surgery</p>
      </div>
      <div class="physician">
        <p class="physician-name">Abena Quist, M.D.</p>
        <p class="physician-specialty">Hip &amp; Knee Replacement/General Orthopaedic Surgery</p>
      </div>
    </section>

    <svg class="footer-shapes" viewBox="0 0 600 200" aria-hidden="true">
      <path d="M0 200 V22 Q0 10 14 10 H28 Q72 10 72 60 V110 Q72 158 122 158 H600 V200 Z" fill="var(--navy)"/>
      <g fill="none" stroke="#fff" stroke-width="2" stroke-linecap="round" stroke-linejoin="round">
        <path d="M30 40 q0 12 12 12 l3 -3 -4 -4 -2 2 q-4 -2 -5 -5 l2 -2 -4 -4 z" fill="#fff" stroke="none"/>
        <rect x="28" y="70" width="18" height="14" rx="2"/>
        <path d="M31 74 h12 M31 78 h12"/>
        <rect x="27" y="99" width="20" height="14" rx="1"/>
        <path d="M27 100 l10 7 10 -7"/>
        <path d="M37 148 c-6 -7 -8 -10 -8 -14 a8 8 0 0 1 16 0 c0 4 -2 7 -8 14 z" fill="#fff" stroke="none"/>
      </g>
      <circle cx="37" cy="134" r="3" fill="var(--navy)"/>
    </svg>

    <ul class="contact">
      <li>954-218-4650</li>
      <li>954-582-1346</li>
      <li>info@myrbspine.com</li>
      <li>18735 North Harlow Pkwy</li>
      <li>NC 27614</li>
    </ul>
  </main>
</body>
</html>
```